brisk-vale.com Real Estate, Investment, Financial corporate

Real Estate, Investment, Financial corporate looking site. Show present a professional firm, with an elegant display. Please see the attached file which includes the logo, palette and fonts.
Updates

We just starting the brief today. ( logo was delayed)

Target Market(s)

Investors, Corporate , B2b

Industry/Entity Type

real-estate investments

Number of Pages Required

3 page

Requirements
Must have
• Dazzling Homepage
Nice to have
• paralex

```html
<!DOCTYPE html>
<html lang="en">
<head>
<meta charset="utf-8">
<title>Brisk-Vale — Real Estate, Investment, Financial corporate</title>
<link rel="stylesheet" href="https://fonts.googleapis.com/css2?family=Montserrat:wght@500;600;700&family=Roboto:wght@400;500&display=swap">
<style>
:root{
  --accent:#cc553c;
  --navy:#27344a;
  --ink:#2f2f2f;
  --muted:#6c6c6c;
  --paper:#ffffff;
  --soft:#f6f6f6;
  --footer:#2a2a2a;
  --line:#cfcfcf;
}
*{box-sizing:border-box;margin:0;padding:0}
html,body{width:1200px;height:3776px;overflow:hidden}
body{position:relative;background:var(--paper);font-family:'Roboto',sans-serif;color:var(--ink)}
.abs{position:absolute}
a{color:inherit;text-decoration:none}

/* header */
.site-header{position:absolute;left:0;top:0;width:1200px;height:91px;background:var(--paper)}
.brand{position:absolute;left:111px;top:22px;font-family:'Montserrat',sans-serif;font-weight:700;font-size:29px;color:var(--ink)}
.main-nav{position:absolute;left:303px;top:33px;display:flex;gap:20px;font-family:'Montserrat',sans-serif;font-weight:500;font-size:17px}
.btn{display:flex;align-items:center;justify-content:center;border-radius:30px;font-family:'Montserrat',sans-serif;font-weight:600;text-transform:uppercase;position:absolute}
.btn-login{left:815px;top:20px;width:109px;height:46px;border:1.5px solid #bbb;color:var(--accent);font-size:16px;gap:5px}
.btn-solid{background:var(--accent);color:#fff}
.btn-invest{left:932px;top:20px;width:152px;height:46px;font-size:16px}

/* hero */
.hero{position:absolute;left:0;top:91px;width:1200px;height:634px;background:linear-gradient(160deg,#20324f 0%,#3e6591 35%,#7aa3c9 55%,#2b4060 80%,#16233a 100%)}
.hero-title{position:absolute;left:0;top:155px;width:1200px;text-align:center;color:#fff;font-family:'Montserrat',sans-serif;font-weight:600;font-size:55px;line-height:68px;text-shadow:0 2px 8px rgba(0,0,0,.35)}
.btn-enquire{left:497px;top:327px;width:206px;height:58px;font-size:19px}

/* services */
.services{position:absolute;left:0;top:0;width:1200px;height:1100px;pointer-events:none}
.service{position:absolute;top:700px;width:300px;text-align:center}
.service h3{font-family:'Montserrat',sans-serif;font-weight:600;font-size:22px;margin-top:20px;color:var(--ink)}
.service p{font-size:15px;line-height:26px;color:var(--muted);margin-top:14px;padding:0 16px}

/* who we are */
.about{position:absolute;left:0;top:1066px;width:1200px;height:534px;background:var(--soft)}
.about-band{position:absolute;left:0;top:960px;width:1200px;height:110px;background:var(--soft)}
.section-title{font-family:'Montserrat',sans-serif;font-weight:600;font-size:43px;color:var(--navy);line-height:50px}
.about-copy{position:absolute;left:111px;top:1203px;width:432px;font-size:15px;line-height:26.5px;color:var(--muted)}
.about-copy p+p{margin-top:27px}
.btn-more{left:111px;top:1446px;width:156px;height:57px;font-size:17px}
.about-photo{position:absolute;left:648px;top:1154px;width:440px;height:373px;background:linear-gradient(135deg,#2c3f5c,#8ea3bd 55%,#e5e8ee)}
.about-tag{position:absolute;left:596px;top:1109px;width:135px;height:127px;background:var(--navy);color:#fff;font-family:'Montserrat',sans-serif;font-weight:600;font-size:20px;line-height:28px;display:flex;align-items:center;justify-content:center;text-align:center}

/* why choose */
.why-title{position:absolute;left:111px;top:1645px}
.why-photo{position:absolute;left:0;top:1785px;width:516px;height:449px;background:linear-gradient(135deg,#c8c2b8,#8a8276 45%,#3d4656 75%,#d9d4cc)}
.why-intro{position:absolute;left:549px;top:1642px;width:530px;color:#fff;font-size:15px;line-height:26px}
.feature{position:absolute;display:flex;align-items:center;gap:21px;color:#fff;font-family:'Montserrat',sans-serif;font-weight:600;font-size:21px;line-height:26px}
.ring{width:98px;height:98px;border:2px solid rgba(255,255,255,.85);border-radius:50%;display:flex;align-items:center;justify-content:center;flex:none}

/* how it works */
.how-title{position:absolute;left:0;top:2305px;width:1200px;text-align:center}
.video{position:absolute;left:111px;top:2373px;width:203px;height:154px;background:var(--navy)}
.steps{position:absolute;left:111px;top:2527px;width:977px;height:229px;border:1.5px solid var(--line)}
.step{position:absolute;top:2570px;width:220px;text-align:center}
.step h4{font-family:'Montserrat',sans-serif;font-weight:600;font-size:22px;margin-top:14px}
.step p{font-size:15px;line-height:25px;color:var(--muted);margin-top:10px}

/* returns */
.returns-photo{position:absolute;left:0;top:2835px;width:800px;height:549px;background:linear-gradient(120deg,#d7dde3,#c9b4a4 35%,#8c5a48 60%,#3b3f4a 85%,#2fb7d9)}
.returns-box{position:absolute;left:652px;top:2914px;width:436px;height:393px;background:var(--navy);color:#fff;padding:40px 46px}
.returns-box h2{font-family:'Montserrat',sans-serif;font-weight:600;font-size:42px;line-height:49px}
.returns-box p{font-size:15px;line-height:26px;margin-top:24px}
.btn-investor{left:694px;top:3198px;width:267px;height:57px;font-size:17px}

/* footer */
.site-footer{position:absolute;left:0;top:3384px;width:1200px;height:392px;background:var(--footer);color:#fff}
.footer-brand{position:absolute;left:111px;top:116px;font-family:'Montserrat',sans-serif;font-weight:700;font-size:43px}
.subscribe{position:absolute;left:111px;top:178px;display:flex;align-items:center;gap:10px;color:var(--accent);font-family:'Montserrat',sans-serif;font-weight:600;font-size:22px}
.col-title{font-family:'Montserrat',sans-serif;font-weight:500;font-size:18px}
.quick{position:absolute;left:463px;top:68px}
.quick ul{list-style:none;margin-top:12px;font-family:'Montserrat',sans-serif;font-size:16px;line-height:28.6px}
.contact{position:absolute;left:710px;top:68px}
.contact li{list-style:none;display:flex;align-items:center;gap:6px;font-size:16px;margin-top:21px}
.contact li:first-child{margin-top:16px}
.rule{position:absolute;left:111px;top:302px;width:977px;height:1px;background:#555}
.copyright{position:absolute;left:111px;top:335px;font-size:15px}
.social{position:absolute;top:322px;width:44px;height:44px;border:1.5px solid #fff;border-radius:50%}
</style>
</head>
<body>

<header class="site-header">
  <div class="brand">Brisk-Vale</div>
  <nav class="main-nav"><a>About</a><a>Real Estate</a><a>Investment</a><a>Financial Corporate</a></nav>
  <a class="btn btn-login"><svg width="12" height="14" viewBox="0 0 12 14"><rect x="1" y="6" width="10" height="8" rx="1" fill="#cc553c"/><path d="M3 6V4a3 3 0 0 1 6 0v2" stroke="#cc553c" stroke-width="2" fill="none"/></svg>Login</a>
  <a class="btn btn-solid btn-invest">Invest Now</a>
</header>

<section class="hero" role="img" aria-label="Glass office towers seen from below against a blue sky">
  <h1 class="hero-title">Brisk-vale Real Estate,<br>Investment, Financial corporate</h1>
  <a class="btn btn-solid btn-enquire">Enquire Now!</a>
</section>

<div class="about-band"></div>
<div class="about"></div>

<svg class="services" viewBox="0 0 1200 1100" aria-hidden="true">
  <defs><filter id="lift" x="-10%" y="-10%" width="120%" height="130%"><feDropShadow dx="0" dy="6" stdDeviation="10" flood-color="#000" flood-opacity=".12"/></filter></defs>
  <polygon points="111,681 396,571 1088,681 1088,971 785,1066 111,971" fill="#fff" filter="url(#lift)"/>
</svg>

<div class="service" style="left:127px">
  <svg width="130" height="90" viewBox="0 0 130 90"><g fill="none" stroke="#2f2f2f" stroke-width="4"><path d="M10 44 L50 8 L78 34"/><path d="M20 36 V84 H72 V60"/><rect x="38" y="58" width="18" height="26"/><path d="M62 18 V10 H70 V26"/></g><circle cx="92" cy="38" r="24" fill="none" stroke="#cc553c" stroke-width="4"/><text x="92" y="48" text-anchor="middle" font-family="Montserrat,sans-serif" font-weight="700" font-size="30" fill="#cc553c">$</text></svg>
  <h3>Real Estate</h3>
  <p>Lorem ipsum dolor sit amet, con sectetur adipiscing elit, sed do eusm od tempor incididu labo.</p>
</div>
<div class="service" style="left:449px">
  <svg width="130" height="90" viewBox="0 0 130 90"><g fill="none" stroke="#2f2f2f" stroke-width="4"><path d="M55 22 Q50 8 65 10 Q80 8 75 22"/><path d="M56 26 Q28 50 38 74 Q46 88 65 88 Q84 88 92 74 Q102 50 74 26 Z"/><rect x="34" y="10" width="16" height="22" rx="2"/></g><text x="66" y="74" text-anchor="middle" font-family="Montserrat,sans-serif" font-weight="700" font-size="32" fill="#cc553c">$</text></svg>
  <h3>Investment</h3>
  <p>Lorem ipsum dolor sit amet, con sectetur adipiscing elit, sed do eusm od tempor incididu labo.</p>
</div>
<div class="service" style="left:770px">
  <svg width="130" height="90" viewBox="0 0 130 90"><circle cx="65" cy="46" r="34" fill="none" stroke="#2f2f2f" stroke-width="3" stroke-dasharray="3 5"/><circle cx="65" cy="46" r="18" fill="none" stroke="#2f2f2f" stroke-width="3.5"/><path d="M47 46 H83 M65 28 V64 M52 36 H78 M52 56 H78" stroke="#2f2f2f" stroke-width="2.5"/><circle cx="65" cy="12" r="9" fill="none" stroke="#cc553c" stroke-width="4"/><circle cx="33" cy="72" r="11" fill="none" stroke="#cc553c" stroke-width="3.5"/><path d="M29 76v-5M33 76v-8M37 76v-3" stroke="#cc553c" stroke-width="2.5"/><circle cx="97" cy="72" r="11" fill="none" stroke="#cc553c" stroke-width="3.5"/><text x="97" y="78" text-anchor="middle" font-family="Montserrat,sans-serif" font-weight="700" font-size="15" fill="#cc553c">$</text></svg>
  <h3>Financial corporate</h3>
  <p>Lorem ipsum dolor sit amet, con sectetur adipiscing elit, sed do eusm od tempor incididu labo.</p>
</div>

<h2 class="section-title abs" style="left:111px;top:1128px">Who We Are</h2>
<div class="about-copy">
  <p>At vero eos et accusamus et iusto odio dignissimos ducims ui blanditiis praesentium voluptatum deleniti atque corrupti dol ores et quas molestias excepturi.</p>
  <p>Sint occaecati cupiditate non provident, similique sunt in cu officia deserunt mollitia animi, id est laborum et dolorum fu arum quidem rerum facilis est et expedita distinctio ptas as da est, omnis dolor repellendus.</p>
</div>
<a class="btn btn-solid btn-more">Read More</a>
<div class="about-photo" role="img" aria-label="Business team reviewing charts and a tablet at a desk"></div>
<div class="about-tag">About<br>Brisk-Vale</div>

<svg class="abs" style="left:0;top:1600px" width="1200" height="562" viewBox="0 0 1200 562" aria-hidden="true"><polygon points="481,0 1200,0 1200,562 516,562 516,185 429,185 413,100" fill="#cc553c"/></svg>
<h2 class="section-title why-title">Why Choose<br>Brisk-Vale</h2>
<div class="why-photo" role="img" aria-label="Couple reviewing documents and a tablet together at home"></div>
<p class="why-intro">Lorem ipsum dolor sit amet, consect etur adipiscing elit, sed do eusm od tempor in cididu labo&nbsp; voluptates repudi i tempora incidunt ut labore et dolore magnam aliquam quaerat volu.</p>

<div class="feature" style="left:547px;top:1757px"><span class="ring"><svg width="36" height="36" viewBox="0 0 36 36"><path d="M6 6h8v12a4 4 0 0 0 8 0V6h8v12a12 12 0 0 1-24 0Z" fill="#fff"/><path d="M6 11h8M22 11h8" stroke="#cc553c" stroke-width="2"/></svg></span>Attractive<br>returns</div>
<div class="feature" style="left:815px;top:1757px"><span class="ring"><svg width="36" height="36" viewBox="0 0 36 36"><circle cx="15" cy="15" r="10" fill="none" stroke="#fff" stroke-width="4"/><path d="M22 22l9 9" stroke="#fff" stroke-width="5" stroke-linecap="round"/></svg></span>Transparent<br>process</div>
<div class="feature" style="left:547px;top:1879px"><span class="ring"><svg width="30" height="36" viewBox="0 0 30 36"><path d="M3 4h24v14c0 9-7 14-12 16C10 32 3 27 3 18Z" fill="#fff"/><path d="M15 8v22c-4-2-8-6-8-12V8Z" fill="#cc553c"/></svg></span>Secure</div>
<div class="feature" style="left:815px;top:1879px"><span class="ring"><svg width="38" height="34" viewBox="0 0 38 34"><path d="M19 2 L37 32 H1 Z" fill="#fff"/><path d="M19 12v10" stroke="#cc553c" stroke-width="4"/><circle cx="19" cy="27" r="2.2" fill="#cc553c"/></svg></span>Risk<br>management</div>
<div class="feature" style="left:547px;top:1999px"><span class="ring"><svg width="38" height="38" viewBox="0 0 38 38"><path d="M8 4v26M2 24l6 8 6-8" stroke="#fff" stroke-width="3.5" fill="none"/><path d="M19 8h6M19 16h10M19 24h14M19 32h18" stroke="#fff" stroke-width="3.5"/></svg></span>Affordable<br>thresholds</div>
<div class="feature" style="left:815px;top:1999px"><span class="ring"><svg width="36" height="36" viewBox="0 0 36 36"><rect x="3" y="15" width="7" height="17" fill="#fff"/><path d="M12 15l6-12c4 0 5 3 4 7l-1 4h9c3 0 4 3 3 5l-3 11c-1 2-2 2-4 2H12Z" fill="#fff"/></svg></span>Convenience</div>

<h2 class="section-title how-title">How It Works</h2>
<div class="video" role="img" aria-label="Video player"><svg class="abs" style="left:69px;top:42px" width="66" height="70" viewBox="0 0 66 70"><path d="M0 0 L66 35 L0 70 Z" fill="#fff"/></svg></div>
<div class="steps"></div>
<svg class="abs" style="left:111px;top:2527px" width="977" height="229" viewBox="0 0 977 229" aria-hidden="true"><g fill="none" stroke="#cfcfcf" stroke-width="1.5"><path d="M229 0 L260 114 L229 229"/><path d="M479 0 L512 114 L479 229"/><path d="M728 0 L761 114 L728 229"/></g></svg>
<div class="step" style="left:123px">
  <svg width="60" height="54" viewBox="0 0 60 54"><rect x="3" y="8" width="42" height="42" rx="3" fill="none" stroke="#cc553c" stroke-width="5"/><path d="M14 26l10 10L54 4" stroke="#cc553c" stroke-width="7" fill="none"/></svg>
  <h4>Select</h4><p>Lorem ipsum dolor sit amet, con tetur adipiscing e</p>
</div>
<div class="step" style="left:378px">
  <svg width="60" height="54" viewBox="0 0 60 54"><path d="M30 4a14 14 0 0 0-8 25v7h16v-7A14 14 0 0 0 30 4Z" fill="none" stroke="#cc553c" stroke-width="4"/><path d="M23 42h14M25 48h10" stroke="#cc553c" stroke-width="4"/></svg>
  <h4>Invest</h4><p>Lorem ipsum dolor sit amet, con tetur adipiscing e</p>
</div>
<div class="step" style="left:618px">
  <svg width="66" height="54" viewBox="0 0 66 54"><rect x="3" y="10" width="60" height="36" fill="none" stroke="#cc553c" stroke-width="5"/><circle cx="33" cy="28" r="12" fill="#cc553c"/><text x="33" y="34" text-anchor="middle" font-family="Roboto,sans-serif" font-weight="500" font-size="16" fill="#fff">1</text><path d="M3 18a8 8 0 0 0 8-8M55 10a8 8 0 0 0 8 8M3 38a8 8 0 0 1 8 8M55 46a8 8 0 0 1 8-8" stroke="#cc553c" stroke-width="3" fill="none"/></svg>
  <h4>Earn</h4><p>Lorem ipsum dolor sit amet, con tetur adipiscing e</p>
</div>
<div class="step" style="left:862px">
  <svg width="66" height="54" viewBox="0 0 66 54"><path d="M4 2v48h60" stroke="#cc553c" stroke-width="4" fill="none"/><rect x="13" y="30" width="8" height="15" fill="#cc553c"/><rect x="25" y="20" width="8" height="25" fill="#cc553c"/><rect x="37" y="26" width="8" height="19" fill="#cc553c"/><rect x="49" y="12" width="8" height="33" fill="#cc553c"/></svg>
  <h4>Profit</h4><p>Lorem ipsum dolor sit amet, con tetur adipiscing e</p>
</div>

<div class="returns-photo" role="img" aria-label="Smiling woman reading a report with charts in a brick-walled office"></div>
<div class="returns-box">
  <h2>Attractive<br>Risk-Adjusted<br>Returns</h2>
  <p>Ut enim ad minima veniam, quis nostrum exerciat ionem ullam corporis suscipit.</p>
</div>
<a class="btn btn-solid btn-investor">Become an Investor</a>

<footer class="site-footer">
  <div class="footer-brand">Brisk-Vale</div>
  <div class="subscribe"><svg width="22" height="16" viewBox="0 0 22 16"><rect x="1" y="1" width="20" height="14" fill="none" stroke="#cc553c" stroke-width="2"/><path d="M1 1l10 8 10-8" fill="none" stroke="#cc553c" stroke-width="2"/></svg>Subscribe</div>
  <div class="quick">
    <div class="col-title">Quick Links</div>
    <ul><li>Home</li><li>About</li><li>Real Estate</li><li>Investment</li><li>Financial corporate</li><li>Contact Us</li></ul>
  </div>
  <div class="contact">
    <div class="col-title">Contact Us</div>
    <ul>
      <li><svg width="10" height="14" viewBox="0 0 10 14"><path d="M5 0a5 5 0 0 0-5 5c0 4 5 9 5 9s5-5 5-9a5 5 0 0 0-5-5Z" fill="#cc553c"/><circle cx="5" cy="5" r="2" fill="#2a2a2a"/></svg>48 Harlow Mill Lane Suite 210</li>
      <li><svg width="12" height="12" viewBox="0 0 12 12"><path d="M2 0l3 3-2 2c1 2 2 3 4 4l2-2 3 3-2 2C5 12 0 7 0 2Z" fill="#cc553c"/></svg>1 555 014 2290</li>
      <li><svg width="13" height="10" viewBox="0 0 13 10"><rect width="13" height="10" fill="#cc553c"/><path d="M0 0l6.5 5L13 0" stroke="#2a2a2a" fill="none"/></svg>info@brisk-vale.com</li>
    </ul>
  </div>
  <div class="rule"></div>
  <div class="copyright">© 2021, Brisk-Vale. All rights reserved.</div>
  <span class="social" style="left:942px" aria-label="Social profile"></span>
  <span class="social" style="left:993px" aria-label="Social profile"></span>
  <span class="social" style="left:1043px" aria-label="Social profile"></span>
</footer>

</body>
</html>
```